HomePage Design for Lumen Getaways - once-in-a-lifetime experiences for busy working people

Design a homepage for the Lumen Getaways (www.lumengetaways.example) website compatible with further web pages and the design briefing documents attached

LG HomePage Design Brief
We are seeking website HomePage designs incorporating our new Logo and colour scheme, for Lumen Getaways (www.lumengetaways.example) to go with the site functionality and wireframe ideas attached.
The website HomePage design needs to
• Incorporate and be consistent with the LG Logo and its colour scheme attached.
• Express the brand values of being inspirational, high quality, upscale, cultured, aspirational, and contemporary – even somewhat ‘hip’. Probably positioned somewhere between Harlow Pike (Deluxe Travel) and Green Walrus (Hip Travel) – see https://www.harlowpike.example and https://www.greenwalrus.example .
• Be instantly recognisable and different from other travel websites and instantly communicate the nature of the brand proposition and target customer base.
• Appeal to our core 25-55 affluent businesspeople demographic
• Work in the UK, US/Canada and Australia/NZ and ultimately in mainland Europe.
• Use fonts and colours that are easily reproduced online and compatible with nearly all browsers.
• Be part of a responsive website design, that can be used both on Desktops and laptops but also with tablets and mobile ‘phones (hence content not too wide across the page)
• Feature the strapline ‘Lumen Getaways in less than 7 Days’
• Work with the and wireframes and processes shown in the attached presentation – although intended as a guide only these features and processes all need to be incorporated into the HomePage.
• Make full use of high quality images and video to convey our brand proposition and products

Target Market(s)

25-55 affluent businesspeople

Industry/Entity Type

Travel Industry

Number of Pages Required

1 page

Font styles to use
Sans Serif

Colors
0455a3
00a88f

Requirements
Must have
• • Incorporate and be consistent with the LG Logo and its colour scheme attached.
• • Express the brand values of being inspirational, high quality, upscale, cultured, aspirational, and contemporary – even somewhat ‘hip’. Probably positioned somewhere between Harlow Pike (Deluxe Travel) and Green Walrus (Hip Travel) – see https://www.harlowpike.example and https://www.greenwalrus.example .
• • Be instantly recognisable and different from other travel websites and instantly communicate the nature of the brand proposition and target customer base.
• • Appeal to our core 25-55 affluent businesspeople demographic
• • Be part of a responsive website design, that can be used both on Desktops and laptops but also with tablets and mobile ‘phones (hence content not too wide across the page)
• • Feature the strapline ‘Lumen Getaways in less than 7 Days’
• • Work with the and wireframes and processes shown in the attached presentation – although intended as a guide only these features and processes all need to be incorporated into the HomePage.
• • Make full use of high quality images and video to convey our brand proposition and products
• Colours as per Logo not as shown below
Nice to have
• • Work in the UK, US/Canada and Australia/NZ and ultimately in mainland Europe.
Should not have
• Must not be cheap or mass-market, nor excessively "stuffy or luxury-orientated"

```html
<!DOCTYPE html>
<html lang="en">
<head>
<meta charset="UTF-8">
<title>Lumen Getaways – Home</title>
<link href="https://fonts.googleapis.com/css2?family=Lato:wght@300;400;700&display=swap" rel="stylesheet">
<style>
:root{
  --navy:#243069;
  --green:#1d5a2e;
  --green-dark:#0f2a18;
  --ink:#1e1e1e;
  --muted:#8a8a8a;
  --grey-band:#ebebeb;
  --white:#ffffff;
  --badge:#d4d4d4;
  --caption:#666666;
}
*{box-sizing:border-box;margin:0;padding:0}
html,body{width:1200px;height:1200px;overflow:hidden;background:var(--white);font-family:'Lato',sans-serif;color:var(--ink)}
.page{position:relative;width:1200px;height:1200px;overflow:hidden}
.abs{position:absolute}
.section-title{font-weight:300;font-size:22px;letter-spacing:.3px;color:var(--ink);text-align:center;white-space:nowrap}
.section-title b{font-weight:700}
.events-band{left:0;top:0;width:1200px;height:106px;background:var(--grey-band)}
.events-band .section-title{position:absolute;left:0;right:0;top:39px}
.event-card{top:162px;width:312px;height:286px;background:var(--white);box-shadow:0 2px 10px rgba(0,0,0,.14);padding:32px 23px 0 23px}
.event-date{position:absolute;top:-18px;left:64px;width:184px;height:40px;background:var(--navy);color:var(--white);font-size:17px;line-height:40px;text-align:center}
.event-title{font-size:18.5px;font-weight:400;line-height:21.5px;color:var(--ink);margin-top:10px}
.event-text{font-size:13.6px;line-height:17.9px;color:var(--muted);text-align:justify;margin-top:13px;hyphens:manual}
.read-more{display:inline-block;font-size:14.5px;color:var(--navy);text-decoration:underline;text-underline-offset:3px;margin-top:14px}
.blog-item{width:320px;height:72px}
.blog-thumb{position:absolute;left:0;top:0;width:71px;height:71px}
.thumb-river{background:linear-gradient(180deg,#8ea08a 0%,#9c8f70 45%,#5d7a3e 75%,#3c5c2a 100%)}
.thumb-family{background:linear-gradient(180deg,#7d9a6a 0%,#b49a7a 50%,#5b6b48 100%)}
.blog-body{position:absolute;left:83px;top:-5px;width:240px}
.blog-title{font-size:15.5px;line-height:21.5px;color:var(--ink)}
.blog-date{font-size:10px;color:#a8a8a8;margin-top:1px;display:flex;align-items:center;gap:2px}
.blog-more{font-size:10.5px;color:var(--navy);text-decoration:underline;margin-top:4px;display:inline-block}
.testimonial{left:766px;top:568px;width:332px;height:205px;background:var(--grey-band);padding:20px 18px 0 18px;text-align:center}
.quote{font-size:13.6px;line-height:21.5px;color:var(--ink)}
.quote-author{text-align:right;font-size:13.6px;font-weight:700;margin-top:-6px;padding-right:6px}
.quote-author span{font-weight:400}
.dots{display:flex;justify-content:center;gap:4px;margin-top:13px}
.dot{width:13px;height:13px;border-radius:50%;border:1.5px solid var(--navy)}
.dot.active{background:var(--navy)}
.stat-band{left:0;top:806px;width:604px;height:95px;background:var(--navy);color:var(--white);text-align:center;padding-top:14px}
.stat-number{font-size:27px;font-weight:700;line-height:32px}
.stat-label{font-size:27px;font-weight:300;line-height:32px}
.newsletter{left:604px;top:806px;width:596px;height:95px;background:var(--green)}
.newsletter-label{position:absolute;left:114px;top:15px;color:var(--white);font-weight:700;font-size:14px;letter-spacing:.1px}
.email-field{position:absolute;left:114px;top:42px;width:299px;height:38px;background:var(--green-dark);color:var(--white);font-size:14px;line-height:38px;padding-left:14px}
.signup-btn{position:absolute;left:413px;top:42px;width:77px;height:38px;background:var(--white);color:var(--ink);font-size:14px;line-height:38px;text-align:center}
.partners{left:0;top:901px;width:1200px;height:133px}
.badge{position:absolute;background:var(--badge)}
.badge-caption{position:absolute;font-size:9.5px;line-height:12px;color:var(--caption);text-align:center;width:120px}
.footer{left:0;top:1034px;width:1200px;height:166px;background:var(--grey-band)}
.footer-col{position:absolute;top:27px}
.footer-head{font-size:17px;font-weight:400;color:var(--ink);white-space:nowrap}
.footer-head b{font-weight:700}
.footer-links{list-style:none;margin-top:13px}
.footer-links li{font-size:14px;line-height:21.6px;color:#6a6a6a;white-space:nowrap}
.contact-row{display:flex;gap:8px;font-size:14px;line-height:21.6px;color:#6a6a6a;margin-top:0}
.contact-row svg{flex:none;margin-top:3px}
</style>
</head>
<body>
<div class="page">

  <section class="abs events-band">
    <h2 class="section-title">TOPICAL <b>EVENTS</b></h2>
  </section>

  <article class="abs event-card" style="left:107px">
    <div class="event-date">DATE : 20-07-2017</div>
    <h3 class="event-title">Trends that drove the market<br>in 2016</h3>
    <p class="event-text">Lorem ipsum dolor sit amet, consectetur adipiscing elit, sed do eiusmod tempor inci-didunt ut labore et dolore magna aliqua. Ut enim ad minim veniam, quis nostrud exerci-tation ullamco laboris nisi ut aliquip ex ea commodo consequat. Duis aute irure dolor in reprehenderit in voluptate velit esse cillum dolore eu fugiat nulla pariatur.</p>
    <span class="read-more">Read More</span>
  </article>
  <article class="abs event-card" style="left:446px">
    <div class="event-date">DATE : 20-07-2017</div>
    <h3 class="event-title">Trends that drove the market<br>in 2016</h3>
    <p class="event-text">Lorem ipsum dolor sit amet, consectetur adipiscing elit, sed do eiusmod tempor inci-didunt ut labore et dolore magna aliqua. Ut enim ad minim veniam, quis nostrud exerci-tation ullamco laboris nisi ut aliquip ex ea commodo consequat. Duis aute irure dolor in reprehenderit in voluptate velit esse cillum dolore eu fugiat nulla pariatur.</p>
    <span class="read-more">Read More</span>
  </article>
  <article class="abs event-card" style="left:785px">
    <div class="event-date">DATE : 20-07-2017</div>
    <h3 class="event-title">Trends that drove the market<br>in 2016</h3>
    <p class="event-text">Lorem ipsum dolor sit amet, consectetur adipiscing elit, sed do eiusmod tempor inci-didunt ut labore et dolore magna aliqua. Ut enim ad minim veniam, quis nostrud exerci-tation ullamco laboris nisi ut aliquip ex ea commodo consequat. Duis aute irure dolor in reprehenderit in voluptate velit esse cillum dolore eu fugiat nulla pariatur.</p>
    <span class="read-more">Read More</span>
  </article>

  <h2 class="abs section-title" style="left:226px;width:400px;top:503px">FROM OUR <b>BLOG</b></h2>
  <h2 class="abs section-title" style="left:730px;width:400px;top:503px">WHAT OUR <b>CLIENTS</b> SAYS</h2>

  <div class="abs blog-item" style="left:107px;top:573px">
    <div class="blog-thumb thumb-river" role="img" aria-label="Photo of a wide river valley with a village and green hills"></div>
    <div class="blog-body"><div class="blog-title">2017’s top travel destinations and experiences</div><div class="blog-date"><svg width="8" height="8" viewBox="0 0 10 10"><circle cx="5" cy="5" r="4" fill="none" stroke="#a8a8a8" stroke-width="1.3"/><path d="M5 2.5V5h2" fill="none" stroke="#a8a8a8" stroke-width="1.1"/></svg>07/20/2017</div><span class="blog-more">Read more</span></div>
  </div>
  <div class="abs blog-item" style="left:432px;top:573px">
    <div class="blog-thumb thumb-river" role="img" aria-label="Photo of a wide river valley with a village and green hills"></div>
    <div class="blog-body"><div class="blog-title">2017’s top travel destinations and experiences</div><div class="blog-date"><svg width="8" height="8" viewBox="0 0 10 10"><circle cx="5" cy="5" r="4" fill="none" stroke="#a8a8a8" stroke-width="1.3"/><path d="M5 2.5V5h2" fill="none" stroke="#a8a8a8" stroke-width="1.1"/></svg>07/20/2017</div><span class="blog-more">Read more</span></div>
  </div>
  <div class="abs blog-item" style="left:107px;top:668px">
    <div class="blog-thumb thumb-family" role="img" aria-label="Photo of a family group posing outdoors on holiday"></div>
    <div class="blog-body"><div class="blog-title">Fun Family Holiday: Boat Cruise Time on the German Rhine</div><div class="blog-date"><svg width="8" height="8" viewBox="0 0 10 10"><circle cx="5" cy="5" r="4" fill="none" stroke="#a8a8a8" stroke-width="1.3"/><path d="M5 2.5V5h2" fill="none" stroke="#a8a8a8" stroke-width="1.1"/></svg>07/20/2017</div><span class="blog-more">Read more</span></div>
  </div>
  <div class="abs blog-item" style="left:432px;top:668px">
    <div class="blog-thumb thumb-family" role="img" aria-label="Photo of a family group posing outdoors on holiday"></div>
    <div class="blog-body"><div class="blog-title">Fun Family Holiday: Boat Cruise Time on the German Rhine</div><div class="blog-date"><svg width="8" height="8" viewBox="0 0 10 10"><circle cx="5" cy="5" r="4" fill="none" stroke="#a8a8a8" stroke-width="1.3"/><path d="M5 2.5V5h2" fill="none" stroke="#a8a8a8" stroke-width="1.1"/></svg>07/20/2017</div><span class="blog-more">Read more</span></div>
  </div>

  <aside class="abs testimonial">
    <p class="quote">"This was one of the most amazing family holi-days we have ever had. We had a wonderful holiday organised within budget by people who knew what they were talking about, who could make relevant recommendations for tours and activities."</p>
    <p class="quote-author"><span>- </span>Priya Halvorsen</p>
    <div class="dots"><span class="dot active"></span><span class="dot"></span><span class="dot"></span></div>
  </aside>

  <div class="abs stat-band">
    <div class="stat-number">5,00,000 +</div>
    <div class="stat-label">Happy Customers</div>
  </div>
  <div class="abs newsletter">
    <div class="newsletter-label">SIGN UP FOR OUR NEWSLETTER</div>
    <div class="email-field">Email</div>
    <div class="signup-btn">SIGN UP</div>
  </div>

  <section class="abs partners" aria-label="Partners and awards">
    <div class="badge" style="left:120px;top:48px;width:76px;height:28px;border-radius:4px"></div>
    <div class="badge" style="left:240px;top:46px;width:108px;height:32px;border-radius:4px"></div>
    <div class="badge" style="left:392px;top:48px;width:178px;height:28px;border-radius:4px"></div>
    <div class="badge" style="left:624px;top:40px;width:56px;height:24px;border-radius:3px"></div>
    <div class="badge-caption" style="left:592px;top:86px">A-List of<br>Travel Agents</div>
    <div class="badge" style="left:735px;top:23px;width:58px;height:58px;border-radius:50%"></div>
    <div class="badge-caption" style="left:704px;top:86px">Online Tour<br>Operator of the Year</div>
    <div class="badge" style="left:860px;top:38px;width:64px;height:26px;border-radius:3px"></div>
    <div class="badge-caption" style="left:833px;top:86px">Top 10 Best<br>Travel Websites</div>
    <div class="badge" style="left:980px;top:42px;width:104px;height:20px;border-radius:3px"></div>
    <div class="badge-caption" style="left:972px;top:86px">Awarded in 2013/14</div>
  </section>

  <footer class="abs footer">
    <div class="footer-col" style="left:106px">
      <h4 class="footer-head">QUICK <b>LINKS</b></h4>
      <ul class="footer-links"><li>About Us</li><li>Our Partners</li><li>FAQs</li><li>Contact Us</li><li>Booking Conditions</li></ul>
    </div>
    <div class="footer-col" style="left:277px">
      <h4 class="footer-head">AWESOME <b>EXPERIENCES</b></h4>
      <ul class="footer-links"><li>World's Greatest Festivals</li><li>Must Do Activites</li><li>Wonders of Wildlife</li><li>Unique Annual Events</li><li>Extraordinary &amp; Secret Places</li></ul>
    </div>
    <div class="footer-col" style="left:588px">
      <h4 class="footer-head">HELPFULL <b>LINKS</b></h4>
      <ul class="footer-links"><li>Financial Protection</li><li>Travel Insurance</li><li>Visas</li><li>Travel Advice</li><li>Group Bookings</li></ul>
    </div>
    <div class="footer-col" style="left:857px">
      <h4 class="footer-head">HOW TO <b>CONTACT US</b></h4>
      <div style="margin-top:12px">
        <div class="contact-row"><svg width="14" height="16" viewBox="0 0 14 18"><path d="M7 1a6 6 0 0 0-6 6c0 4.5 6 10 6 10s6-5.5 6-10a6 6 0 0 0-6-6z" fill="none" stroke="#555" stroke-width="1.8"/><circle cx="7" cy="7" r="2.2" fill="#555"/></svg><span>18-20 Marlow Row, Eastbridge,<br>United Kingdom</span></div>
        <div class="contact-row" style="margin-top:6px"><svg width="14" height="14" viewBox="0 0 16 16"><path d="M3 1l3 3-1.6 2.2c1 2 2.4 3.4 4.4 4.4L11 9l3 3-2 2.5C6 14 2 10 1.5 3z" fill="#555"/></svg><span>+44 80090017</span></div>
        <div class="contact-row" style="margin-top:11px"><svg width="18" height="14" viewBox="0 0 18 14"><rect x="1" y="1" width="16" height="12" fill="none" stroke="#555" stroke-width="1.6"/><path d="M1 1l8 7 8-7" fill="none" stroke="#555" stroke-width="1.6"/></svg><span>support@lumengetaways.example</span></div>
      </div>
    </div>
  </footer>

</div>
</body>
</html>
```